Stylish High End Wedding Videography/Films Website (BDMR)

We need a modern and high-end website look for our wedding video and films business. We films weddings all over the United Kingdom and at European destinations so need something to reflect our work. The website should be visually stunning with images and videos being the focal point as this is what our services are;

I have uploads of some items I like and the features the site needs to have. These have been taken from other websites using standout features.

We need the following pages;

1 - Homepage
2 - Films Index Page
3 - Individual Films Page
4 - Prices / Collection Page
5 - Reviews
6 - Options
7 - About
8 - Contact
9 - Blog Index
10 - Blog Page

All pages must be consistent so have a similar style.

Pages on menu:
Films
Prices
Reviews
Options
About
Contact

We require a responsive look too. Over 90% of our visitors access the website via their mobile devices.

Please use the colours from our logo to incorporate into the website.

Target Market(s)

Wedding Couples

Industry/Entity Type

Wedding Photography

Number of Pages Required

5+ page

Font styles to use
Sans Serif
Script

Requirements
Must have
• The logo must be in the centre of the menu at the top.

Social icons at the bottom of the page.

Use only two fonts including Lore which is supplied
Nice to have
• Different video for each page on the top header. This will play behind the menu.

```html
<!DOCTYPE html>
<html lang="en">
<head>
<meta charset="utf-8">
<title>BDMR Wedding Films</title>
<link href="https://fonts.googleapis.com/css2?family=Josefin+Sans:wght@400;600;700&family=Lato:wght@400;700&display=swap" rel="stylesheet">
<style>
:root{
  --gold:#b09a64;
  --gold-dark:#9c864f;
  --ink:#2b2b2b;
  --charcoal:#232323;
  --grey:#7a7a7a;
  --light:#f4f2ee;
  --white:#ffffff;
  --base:#3b352f;
}
*{margin:0;padding:0;box-sizing:border-box}
html,body{width:1200px;height:4320px;overflow:hidden}
body{font-family:"Lato",Arial,sans-serif;color:var(--ink);background:var(--white);position:relative}
.head{font-family:"Josefin Sans",Arial,sans-serif;font-weight:700;letter-spacing:2px;text-transform:uppercase}
section,header,footer{position:absolute;left:0;width:1200px}
.media{position:absolute}
.btn{display:inline-block;font-family:"Josefin Sans",Arial,sans-serif;font-weight:700;font-size:14px;letter-spacing:1.5px;text-transform:uppercase;padding:14px 26px 11px;border-radius:24px}
.btn-dark{background:var(--charcoal);color:var(--white)}
.btn-gold{background:var(--gold);color:var(--white)}

/* hero */
.hero{top:0;height:672px;overflow:hidden}
.hero-photo{inset:0;background:linear-gradient(180deg,#e9ecec 0%,#d8d8cf 30%,#b7a07a 55%,#a5874f 72%,#8c6f3e 100%)}
.nav{position:absolute;top:0;left:0;width:1200px;height:70px;display:flex;align-items:center;justify-content:center;gap:0}
.nav ul{display:flex;list-style:none;gap:34px}
.nav li{font-family:"Josefin Sans",Arial,sans-serif;font-weight:600;font-size:13px;letter-spacing:1.5px;color:var(--white)}
.nav .brand{width:170px;text-align:center;font-family:"Josefin Sans",Arial,sans-serif;font-weight:700;font-size:24px;letter-spacing:4px;color:var(--gold);background:var(--white);padding:22px 0 16px;margin:0 36px;align-self:flex-start}
.hero-title{position:absolute;top:380px;left:0;width:1200px;text-align:center;font-size:46px;line-height:58px;color:#3c3c3c}
.hero-title span{color:var(--gold)}

/* intro */
.intro{top:672px;height:388px;background:var(--gold)}
.intro-text{position:absolute;left:160px;top:92px;width:440px;color:var(--white)}
.intro-text h2{font-size:34px;margin-bottom:22px}
.intro-text p{font-size:13px;line-height:20px;margin-bottom:14px}
.intro-text .btn{margin-top:8px}
.portrait{left:648px;top:56px;width:392px;height:272px;background:linear-gradient(135deg,#e8e6e3,#bfb8b0 60%,#8a8179)}

/* about */
.about{top:1060px;height:332px;background:var(--white)}
.about-text{position:absolute;left:300px;top:64px;width:600px;text-align:center;color:var(--grey);font-size:12px;line-height:20px}
.about-text p{margin-bottom:14px}

/* alt */
.alt{top:1392px;height:368px;background:var(--charcoal)}
.alt-photo{left:0;top:0;width:440px;height:368px;background:linear-gradient(120deg,#6b6650,#9a9074 45%,#3e3b32)}
.alt-text{position:absolute;left:490px;top:92px;width:300px;color:var(--white)}
.alt-text h2{font-size:30px;line-height:38px;color:var(--gold);margin-bottom:14px}
.alt-text p{font-size:12px;line-height:18px;margin-bottom:18px;color:#d8d8d8}

/* stories */
.stories{top:1760px;height:600px;background:var(--white)}
.stories h2{position:absolute;top:80px;width:1200px;text-align:center;font-size:32px;color:var(--gold)}
.stories h2 span{color:var(--ink)}
.slide-side{top:160px;height:320px;width:248px;background:linear-gradient(160deg,#e9e4df,#cdc4bd);opacity:.85}
.slide-left{left:0}
.slide-right{left:952px}
.slide-main{left:280px;top:140px;width:640px;height:380px;background:linear-gradient(180deg,#d9dcd7,#b9b6ac 55%,#6d6a62)}
.slide-caption{position:absolute;left:280px;top:440px;width:640px;text-align:center;font-size:24px;color:var(--white)}
.slide-nav{position:absolute;top:440px;font-size:22px;color:var(--ink)}
.prev{left:190px}.next{left:948px}

/* engagement */
.gallery{top:2360px;height:472px;background:var(--white)}
.gallery-photo{left:560px;top:40px;width:640px;height:372px;background:linear-gradient(110deg,#d4cec6,#a2988c 50%,#6f655a)}
.gallery-text{position:absolute;left:160px;top:0}
.gallery-text .kicker{position:absolute;top:40px;font-size:13px;line-height:18px;color:var(--grey);letter-spacing:1.5px;width:200px}
.gallery-text h2{position:absolute;top:318px;font-size:32px;line-height:40px;width:300px}
.gallery-text h2 span{color:var(--gold)}
.gallery-arrow{position:absolute;left:540px;top:306px;width:40px;height:40px;border-radius:50%;background:var(--charcoal)}

/* feedback */
.feedback{top:2832px;height:528px;overflow:hidden}
.feedback-photo{inset:0;background:linear-gradient(90deg,#cfd2d3 0%,#e6e6e4 35%,#c9cfd2 65%,#8fa1ab 100%)}
.feedback h2{position:absolute;left:640px;top:72px;font-size:32px;color:var(--gold)}
.feedback h2 span{color:var(--ink)}
.quote-box{position:absolute;left:660px;top:170px;width:280px;height:280px;transform:rotate(45deg);background:var(--white)}
.quote-text{position:absolute;left:680px;top:210px;width:240px;text-align:center}
.quote-text .mark{font-family:Georgia,serif;font-size:64px;line-height:50px;color:var(--ink)}
.quote-text p{font-size:11px;line-height:17px;color:var(--grey);margin:14px 0 10px}
.quote-text .name{font-family:"Josefin Sans",Arial,sans-serif;font-size:11px;font-weight:700;letter-spacing:1px}
.q-arrow{position:absolute;top:290px;width:28px;height:28px;background:var(--charcoal)}
.q-prev{left:626px}.q-next{left:946px}

/* cta */
.cta{top:3360px;height:300px;background:var(--gold);text-align:center;color:var(--white)}
.cta h2{padding-top:70px;font-size:38px;line-height:48px}
.cta p{font-size:12px;margin:8px 0 16px}

/* footer */
.footer{top:3660px;height:580px;background:var(--white)}
.insta{position:absolute;left:160px;top:74px;width:300px;text-align:center}
.insta h3{font-size:22px;color:var(--ink);margin-bottom:22px}
.insta-row{display:flex;gap:12px;justify-content:center}
.insta-row .thumb{width:88px;height:88px}
.t1{background:linear-gradient(135deg,#c8d6dc,#a69b86)}
.t2{background:linear-gradient(135deg,#a9b59a,#e9e6e0)}
.t3{background:linear-gradient(135deg,#d8d2c7,#7c8a6e)}
.news{position:absolute;left:640px;top:74px;width:400px;text-align:center}
.news h3{font-size:22px;color:var(--gold);margin-bottom:14px}
.news h3 span{color:var(--ink)}
.news p{font-size:11px;color:var(--grey);margin-bottom:16px}
.news .field{margin:0 auto 14px;width:380px;height:40px;border-radius:20px;background:var(--light);text-align:left;padding:13px 20px;font-size:12px;color:#9a9a9a}
.footer-brand{position:absolute;top:296px;width:1200px;text-align:center;font-family:"Josefin Sans",Arial,sans-serif;font-weight:700;font-size:28px;letter-spacing:5px;color:var(--gold)}
.footer-links{position:absolute;top:382px;width:1200px;display:flex;justify-content:center;gap:40px;list-style:none;font-family:"Josefin Sans",Arial,sans-serif;font-size:11px;letter-spacing:1.5px;color:var(--grey)}
.contact-line{position:absolute;width:1200px;text-align:center;font-size:12px;color:var(--grey)}
.contact-line b{color:var(--gold)}
.l1{top:418px}.l2{top:440px}
.social{position:absolute;top:484px;width:1200px;display:flex;justify-content:center;gap:14px}
.social span{width:34px;height:34px;border-radius:50%;background:var(--gold)}
.base{top:4240px;height:80px;background:var(--base);color:#cfc7bb;text-align:center;font-size:11px;line-height:80px;letter-spacing:1px}
</style>
</head>
<body>

<header class="hero">
  <div class="media hero-photo" role="img" aria-label="Bride and groom standing in a golden wheat field at sunset"></div>
  <nav class="nav">
    <ul><li>HOME</li><li>FILMS</li><li>WEDDINGS</li><li>PRICES</li></ul>
    <div class="brand">BDMR</div>
    <ul><li>REVIEWS</li><li>OPTIONS</li><li>ABOUT</li><li>CONTACT</li></ul>
  </nav>
  <h1 class="hero-title head">Wedding Videography<br>- North East, UK and<br><span>Worldwide Films</span></h1>
</header>

<section class="intro">
  <div class="intro-text">
    <h2 class="head">Hey I'm Ben Dalmore</h2>
    <p>I'm a filmmaker who loves telling honest stories from the first look to the last dance, capturing every emotion in a calm, cinematic way.</p>
    <p>Based in the North East, I travel across the UK and Europe to film weddings, elopements and celebrations with a relaxed, friendly approach.</p>
    <span class="btn btn-dark">Learn More</span>
  </div>
  <div class="media portrait" role="img" aria-label="Portrait of the filmmaker"></div>
</section>

<section class="about">
  <div class="about-text">
    <p>Ben Dalmore is a wedding filmmaker based in the North East of England, creating timeless films for couples who want their day remembered exactly as it felt, with natural sound, real moments and gentle storytelling.</p>
    <p>Every film is shaped around you. From quiet vows in a country chapel to a sunset celebration abroad, I stay in the background and let the day unfold naturally while capturing the details you may have missed.</p>
    <p>After the wedding, each film is carefully edited with music, speeches and laughter woven together, so you can relive the emotion of your story for years to come and share it with the people you love most.</p>
  </div>
</section>

<section class="alt">
  <div class="media alt-photo" role="img" aria-label="Couple kissing under greenery"></div>
  <div class="alt-text">
    <h2 class="head">Prefer something a bit more funky?</h2>
    <p>If you are a couple who prefers something a bit different to the norm, please check out my alternative option.</p>
    <span class="btn btn-gold">Watch Now</span>
  </div>
</section>

<section class="stories">
  <h2 class="head">Stories <span>of Ben Dalmore</span></h2>
  <div class="media slide-side slide-left" role="img" aria-label="Bride in a white gown outdoors"></div>
  <div class="media slide-main" role="img" aria-label="Wedding ceremony with bridesmaids and groomsmen under a floral arch"></div>
  <div class="media slide-side slide-right" role="img" aria-label="Bridesmaids in pink dresses"></div>
  <div class="slide-caption head">Lena + Marcus</div>
  <div class="slide-nav prev head">Prev</div>
  <div class="slide-nav next head">Next</div>
</section>

<section class="gallery">
  <div class="media gallery-photo" role="img" aria-label="Engaged couple embracing with a bouquet"></div>
  <div class="gallery-text">
    <div class="kicker head">Explore<br>my favorite<br>images</div>
    <h2 class="head"><span>Wedding</span><br>Engagement</h2>
  </div>
  <svg class="gallery-arrow" viewBox="0 0 40 40" aria-hidden="true"><path d="M17 14l6 6-6 6" fill="none" stroke="#fff" stroke-width="2"/></svg>
</section>

<section class="feedback">
  <div class="media feedback-photo" role="img" aria-label="Bride in a lace gown by the sea"></div>
  <h2 class="head">Client's <span>Feedback</span></h2>
  <div class="quote-box"></div>
  <svg class="q-arrow q-prev" viewBox="0 0 28 28" aria-hidden="true"><path d="M16 9l-5 5 5 5" fill="none" stroke="#fff" stroke-width="2"/></svg>
  <svg class="q-arrow q-next" viewBox="0 0 28 28" aria-hidden="true"><path d="M12 9l5 5-5 5" fill="none" stroke="#fff" stroke-width="2"/></svg>
  <div class="quote-text">
    <div class="mark">&ldquo;</div>
    <p>Ben captured our day so beautifully. Watching our film brings back every feeling, every laugh and every tear. We could not recommend him more.</p>
    <div class="name">- CLIENT'S NAME</div>
  </div>
</section>

<section class="cta">
  <h2 class="head">You Matter.<br>Your Story Matters.</h2>
  <p>Let's create your film</p>
  <span class="btn btn-dark">Contact Me</span>
</section>

<footer class="footer">
  <div class="insta">
    <h3 class="head">@bdmrfilms</h3>
    <div class="insta-row">
      <div class="thumb t1" role="img" aria-label="Couple on a beach"></div>
      <div class="thumb t2" role="img" aria-label="Couple in a garden"></div>
      <div class="thumb t3" role="img" aria-label="Bridal bouquet"></div>
    </div>
  </div>
  <div class="news">
    <h3 class="head">Stay <span>Updated</span></h3>
    <p>Join the list for news, offers and latest wedding films.</p>
    <div class="field">Email Address...</div>
    <span class="btn btn-gold">Subscribe Now</span>
  </div>
  <div class="footer-brand">BDMR</div>
  <ul class="footer-links"><li>BLOG</li><li>FILMS</li><li>HOME</li><li>PRICES</li><li>REVIEWS</li><li>OPTIONS</li><li>ABOUT</li><li>CONTACT</li></ul>
  <div class="contact-line l1"><b>Email :</b> hello@bdmrfilms.co.uk</div>
  <div class="contact-line l2"><b>Phone :</b> 07700 900 123</div>
  <div class="social" aria-label="Social links"><span></span><span></span><span></span></div>
</footer>

<section class="base">Copyright &copy; BDMR WEDDING FILMS - 2024. All Rights Reserved.</section>

</body>
</html>
```